Finance Product Agency Business Card Design

We're an agency that provides products (service contracts, gap insurance, tire and wheel, etc) and support to dealership finance departments. We specialize in training finance producers to maximize their potential and also keep them up to date on the ever changing compliance and legal landscape. I'll attach an image of our logo, excited to see what you all come up with. Would also be interested in discussing our new website design with the winner.

Target Market(s)

auto dealerships

Industry/Entity Type

Business

Contact Information for Business Card

Mark Dolvery
Phone 317.624.5583
Fax 855.472.3308
email Mark.Dolvery@brightlanecoverage.example

Requirements
Must have
• basic contact information
Nice to have
• looking for something professional but modern

```html
<!DOCTYPE html>
<html lang="en">
<head>
<meta charset="utf-8">
<title>Brightlane Coverage – Business Card</title>
<link rel="stylesheet" href="https://fonts.googleapis.com/css2?family=Open+Sans:wght@400;600;700;800&display=swap">
<style>
  :root {
    --teal: #3f6f82;
    --teal-dark: #2f5566;
    --teal-light: #55879a;
    --paper: #f6f6f4;
    --ink: #1f4d5f;
    --black: #111417;
    --backdrop: #e7e4df;
    --white: #ffffff;
  }
  * { box-sizing: border-box; margin: 0; padding: 0; }
  html, body {
    width: 1200px; height: 780px; overflow: hidden;
    background: var(--backdrop);
    font-family: "Open Sans", Arial, sans-serif;
  }
  .sheet {
    width: 1200px; height: 780px;
    display: flex; align-items: center; justify-content: center; gap: 44px;
  }
  .card {
    position: relative;
    width: 540px; height: 309px;
    border-radius: 4px;
    overflow: hidden;
    box-shadow: 0 10px 26px rgba(0,0,0,.18), 0 2px 4px rgba(0,0,0,.12);
  }

  /* Front */
  .card-front { background: var(--paper); }
  .front-sweep { position: absolute; inset: 0; width: 100%; height: 100%; }
  .holder-name {
    position: absolute; left: 26px; bottom: 40px;
    color: var(--white); font-weight: 700; font-size: 17px;
    letter-spacing: .04em; text-transform: uppercase;
    white-space: nowrap;
  }
  .brand-front {
    position: absolute; left: 236px; top: 40px;
    display: flex; align-items: center; gap: 12px;
  }
  .brand-dot {
    width: 34px; height: 34px; border-radius: 50%;
    background: var(--teal); flex: none;
  }
  .brand-name {
    font-weight: 800; color: var(--ink);
    font-size: 22px; line-height: 1.05; text-transform: uppercase;
    letter-spacing: .01em;
  }
  .contact-lines {
    position: absolute; right: 24px; top: 138px;
    display: flex; flex-direction: column; align-items: flex-end; gap: 6px;
  }
  .contact-line {
    display: flex; align-items: center; gap: 8px;
    color: var(--ink); font-size: 14px; font-weight: 600;
  }
  .contact-icon {
    width: 16px; height: 16px; background: var(--teal);
    border-radius: 2px; display: flex; align-items: center; justify-content: center;
  }
  .contact-email {
    position: absolute; right: 24px; bottom: 24px;
    color: var(--ink); font-size: 12px; font-weight: 600;
    white-space: nowrap;
  }

  /* Back */
  .card-back {
    background: radial-gradient(ellipse at 50% 50%, var(--teal-light) 0%, var(--teal) 55%, var(--teal-dark) 100%);
  }
  .back-texture {
    position: absolute; inset: 0;
    background: linear-gradient(135deg, rgba(255,255,255,.05) 0%, rgba(255,255,255,0) 45%, rgba(0,0,0,.08) 100%);
  }
  .brand-back {
    position: absolute; inset: 0;
    display: flex; align-items: center; justify-content: center; gap: 16px;
  }
  .brand-back .brand-dot {
    width: 52px; height: 52px; background: var(--white);
  }
  .brand-back .brand-name {
    color: var(--white); font-size: 34px;
  }
</style>
</head>
<body>
<main class="sheet">

  <section class="card card-front" aria-label="Business card front">
    <svg class="front-sweep" viewBox="0 0 540 309" preserveAspectRatio="none" aria-hidden="true">
      <defs>
        <linearGradient id="sweepTeal" x1="0" y1="0" x2="1" y2="1">
          <stop offset="0" stop-color="#4a7d90"/>
          <stop offset="1" stop-color="#345d6e"/>
        </linearGradient>
      </defs>
      <path d="M0,0 L160,0 C112,110 132,230 212,309 L0,309 Z" fill="url(#sweepTeal)"/>
      <path d="M160,0 C112,110 132,230 212,309 L228,309 C146,230 126,110 172,0 Z" fill="#111417"/>
      <path d="M172,0 C126,110 146,230 228,309 L235,309 C152,230 132,110 178,0 Z" fill="#d9dcdd"/>
    </svg>

    <p class="holder-name">Mark Dolvery</p>

    <div class="brand-front">
      <span class="brand-dot"></span>
      <p class="brand-name">Brightlane<br>Coverage</p>
    </div>

    <div class="contact-lines">
      <p class="contact-line">317.624.5583
        <span class="contact-icon">
          <svg width="10" height="10" viewBox="0 0 10 10" aria-hidden="true"><path d="M2 1 L4 1 L4.6 3 L3.4 3.8 Q4.4 5.8 6.2 6.6 L7 5.4 L9 6 L9 8 Q9 9 8 9 Q1 8.4 1 2 Q1 1 2 1 Z" fill="#fff"/></svg>
        </span>
      </p>
      <p class="contact-line">855.472.3308
        <span class="contact-icon">
          <svg width="10" height="10" viewBox="0 0 10 10" aria-hidden="true"><rect x="2.5" y="1" width="5" height="3" fill="#fff"/><rect x="1" y="4" width="8" height="4" rx="1" fill="#fff"/><rect x="2.5" y="7" width="5" height="2" fill="#fff"/></svg>
        </span>
      </p>
    </div>

    <p class="contact-email">Mark.Dolvery@brightlanecoverage.example</p>
  </section>

  <section class="card card-back" aria-label="Business card back">
    <div class="back-texture" role="img" aria-label="Soft teal background texture"></div>
    <div class="brand-back">
      <span class="brand-dot"></span>
      <p class="brand-name">Brightlane<br>Coverage</p>
    </div>
  </section>

</main>
</body>
</html>
```